Brookvale Harbour Clinic advertising

I have a copy that we had done several years ago. I loved it and still do. Unfortunately, the original graphic designer lost the original artwork. What I do have is the same artwork at a small fridge magnet size. I need to new artwork to look like the small magnet version.
The main brief is to appeal to our clients who have addiction problems. It needs to be edgy and as far removed from the typical medical center images

Requirements
Must have
• The print quality must be able to be blown up to 1m x 2m.

```html
<!DOCTYPE html>
<html lang="en">
<head>
<meta charset="utf-8">
<title>Brookvale Harbour Clinic – Heroin Poster</title>
<link href="https://fonts.googleapis.com/css2?family=Roboto+Condensed:wght@300;400;500;600&family=Source+Sans+3:wght@600&display=swap" rel="stylesheet">
<style>
  :root {
    --page-bg: #d8d5d1;
    --poster-black: #0c0c0c;
    --heroin-orange: #e8922a;
    --help-teal: #5f9e86;
    --text-white: #ececec;
    --photo-light: #cdb8a0;
    --photo-mid: #8c7560;
    --photo-dark: #2f261e;
  }
  * { margin: 0; padding: 0; box-sizing: border-box; }
  html, body {
    width: 1200px;
    height: 960px;
    overflow: hidden;
    background: var(--page-bg);
  }
  .poster {
    position: absolute;
    left: 360px;
    top: 30px;
    width: 480px;
    height: 900px;
    background: var(--poster-black);
    overflow: hidden;
  }
  .poster__photo {
    position: absolute;
    left: 0;
    top: 18px;
    width: 476px;
    height: 480px;
    clip-path: polygon(0 0, 100% 0, 82% 96%, 0 100%);
    background:
      radial-gradient(ellipse 45% 40% at 55% 55%, var(--photo-light) 0%, transparent 70%),
      linear-gradient(180deg, var(--photo-mid) 0%, #a08a72 45%, var(--photo-dark) 100%);
  }
  .poster__web {
    position: absolute;
    left: 458px;
    top: 466px;
    transform: rotate(-90deg);
    transform-origin: left top;
    font-family: "Roboto Condensed", sans-serif;
    font-weight: 400;
    font-size: 14px;
    letter-spacing: 0.6px;
    color: var(--heroin-orange);
    white-space: nowrap;
  }
  .poster__headline {
    position: absolute;
    left: 0;
    top: 490px;
    width: 480px;
    height: 150px;
    display: block;
  }
  .poster__headline text {
    font-family: "Source Sans 3", sans-serif;
    font-weight: 600;
    font-size: 182px;
    fill: var(--heroin-orange);
  }
  .poster__tagline {
    position: absolute;
    left: 0;
    top: 652px;
    width: 480px;
    text-align: center;
    font-family: "Roboto Condensed", sans-serif;
    font-weight: 500;
    font-size: 30px;
    line-height: 36px;
    color: var(--text-white);
  }
  .poster__phone {
    position: absolute;
    left: 0;
    top: 692px;
    width: 480px;
    text-align: center;
    font-family: "Roboto Condensed", sans-serif;
    font-weight: 600;
    font-size: 68px;
    line-height: 76px;
    color: var(--help-teal);
  }
  .poster__clinic {
    position: absolute;
    left: 0;
    top: 798px;
    width: 480px;
    text-align: center;
    font-family: "Roboto Condensed", sans-serif;
    font-weight: 500;
    font-size: 26px;
    line-height: 32px;
    color: var(--help-teal);
  }
  .poster__offer {
    position: absolute;
    left: 0;
    top: 838px;
    width: 480px;
    text-align: center;
    font-family: "Roboto Condensed", sans-serif;
    font-weight: 300;
    font-size: 25px;
    line-height: 32px;
    color: var(--text-white);
  }
</style>
</head>
<body>
  <main class="poster">
    <div class="poster__photo" role="img" aria-label="Moody close-up photograph in warm sepia tones"></div>
    <div class="poster__web">www.brookvaleharbour.com.au</div>
    <svg class="poster__headline" viewBox="0 0 480 150" aria-label="HEROIN">
      <text x="0" y="134" textLength="480" lengthAdjust="spacingAndGlyphs">HEROIN</text>
    </svg>
    <p class="poster__tagline">Got a problem? We Can Help.</p>
    <p class="poster__phone">0295550147</p>
    <p class="poster__clinic">Brookvale Harbour Clinic</p>
    <p class="poster__offer">Free Treatment Available</p>
  </main>
</body>
</html>
```